Explainer Video Landing Page

We will soon have an "explainer" video which will explain to people in a graphical way what it is we do and the solutions we provide. Our current landing page design, located at http://www.lanternvoicecentral.com has a lot of different elements that we like, but won't focus on the new video we have as the "hero". We will want this new landing page to really showcase the video. Some of the other design elements we need are :
1- A link to "Get a Quote Online", in some way. This is the "goal" of the landing page.
2- We'll want some content sections under the video
3- We'll want the lead gen form to be there as well.
As an example, have a look at what BrisklyFern did. http://www.brisklyfern.com/
We like their example, but find it a bit busy. Our design should be cleaner with more whitespace. They are doing a lot of good things on that page that we'll want to mimic, like adding testimonials and existing customer logos.
Thank you in advance for participating in our design project.
Target Market(s)
Small and Mid-size Businesses. This will be a B2B landing page, focused on the communications needs of business.
Look and feel
Each slider illustrates characteristics of the customer's brand and the style your logo design should communicate.

```html
<!DOCTYPE html>
<html lang="en">
<head>
<meta charset="utf-8">
<title>Corvella – Hosted PBX</title>
<link rel="stylesheet" href="https://fonts.googleapis.com/css2?family=Jost:wght@400;500;600;700&family=Arimo:ital,wght@0,400;0,700;1,400&display=swap">
<style>
:root{
  --teal:#00a48a;
  --teal-dark:#008f78;
  --orange:#f07620;
  --orange-dark:#c85c12;
  --pink:#e8197a;
  --ink:#222;
  --body:#555;
  --grey-bg:#efefef;
  --line:#d6d6d6;
  --black:#000;
  --white:#fff;
}
*{margin:0;padding:0;box-sizing:border-box}
html,body{width:1200px;height:2214px;overflow:hidden;background:var(--white)}
body{position:relative;font-family:"Arimo",Arial,sans-serif;color:var(--body)}
.abs{position:absolute}

/* header */
.brand{left:0;width:1200px;top:22px;text-align:center}
.brand-mark{display:block;margin:0 auto 12px;width:34px;height:34px;border-radius:50%;background:#222}
.brand-name{font-family:"Jost",sans-serif;font-weight:600;font-size:18px;letter-spacing:6px;color:#111}
.main-nav{top:115px;left:0;width:1200px;height:39px;background:var(--teal);border-bottom:1px solid var(--teal-dark)}
.main-nav ul{list-style:none;display:flex;position:absolute;left:223px;width:751px;height:39px}
.main-nav li{flex:1;text-align:center;line-height:39px;font-size:12px;color:var(--white);border-right:1px solid rgba(255,255,255,.18)}
.main-nav li.is-active{background:var(--teal-dark)}

/* hero */
.hero{top:154px;left:0;width:1200px;height:594px;background:linear-gradient(#f4f4f4,#fff 20%)}
.hero-band{left:0;top:0;width:1200px;height:594px}
.video{left:242px;top:47px;width:715px;height:379px;background:#000;padding:7px;box-shadow:0 18px 14px -10px rgba(90,45,10,.6)}
.video-frame{width:100%;height:100%;background:radial-gradient(ellipse at 60% 40%,#5a5a5a,#2b2b2b 60%,#161616);position:relative}
.video-play{position:absolute;left:318px;top:128px}
.video-bar{position:absolute;left:0;bottom:0;width:100%;height:20px;background:#1b1b1b;color:#999;font-size:8px;line-height:20px;padding-left:68px}
.hero-title{left:241px;top:628px;width:440px;white-space:nowrap;font-family:"Jost",sans-serif;font-weight:700;color:var(--white);font-size:39px;line-height:40px;letter-spacing:-.6px}
.hero-sub{left:241px;top:668px;width:440px;white-space:nowrap;font-family:"Jost",sans-serif;font-weight:700;color:#111;font-size:22.5px;line-height:26px;letter-spacing:-.4px}
.quote-btn{left:701px;top:636px;width:254px;height:56px;background:var(--pink);border-radius:4px;color:var(--white);font-family:"Jost",sans-serif;font-weight:600;font-size:19px;text-align:center;line-height:56px;box-shadow:0 2px 3px rgba(0,0,0,.25);white-space:nowrap}

/* welcome */
.welcome{top:748px;left:0;width:1200px;height:222px;background:var(--grey-bg)}
.welcome-mark{left:578px;top:-14px;width:44px;height:44px;border-radius:50%;background:#222}
.section-title{left:0;width:1200px;text-align:center;font-family:"Jost",sans-serif;font-weight:500;font-size:20px}
.welcome .section-title{top:64px;color:var(--orange)}
.welcome-copy{left:236px;top:114px;width:732px;text-align:center;font-size:11.5px;line-height:18px}

/* clients */
.clients{top:970px;left:0;width:1200px;height:251px}
.clients-divider{left:74px;top:0;width:1052px;height:2px;background:#fff;box-shadow:0 -1px 0 #e6e6e6}
.clients .section-title{top:36px;color:var(--teal);font-size:18px}
.clients-lead{left:0;top:69px;width:1200px;text-align:center;font-size:19.5px;line-height:27px;color:#333}
.client-logo{top:150px;width:103px;height:52px;border:2px solid #e2e2e2;background:var(--white);display:flex;align-items:center;justify-content:center;gap:5px;font-weight:700;font-size:14px;color:#555;white-space:nowrap}
.client-logo i{width:8px;height:8px;border-radius:50%;background:#999;display:block}

/* demo form */
.demo{top:1221px;left:0;width:1200px;height:295px;background:var(--teal);color:var(--white)}
.demo .section-title{top:38px;color:var(--white);font-weight:600}
.demo-copy{left:236px;top:74px;width:728px;text-align:center;font-size:12px;line-height:22px}
.field{width:231px;height:39px;background:var(--white);border:1px solid #cfcfcf;color:#777;font-size:12px;line-height:37px;padding-left:9px}
.demo-btn{left:726px;top:200px;width:233px;height:39px;background:linear-gradient(#4a4a4a,#111);color:var(--white);font-family:"Jost",sans-serif;font-weight:600;font-size:17px;text-align:center;line-height:39px;border-radius:2px}

/* testimonials */
.testimonials{top:1516px;left:0;width:1200px;height:454px}
.testimonials .section-title{top:36px;color:var(--orange)}
.testimonial{top:91px;width:230px;height:318px;border:2px solid #dedede;background:var(--white);box-shadow:0 1px 2px rgba(0,0,0,.08);overflow:hidden}
.testimonial-quotes{position:absolute;left:8px;top:-18px;width:210px;display:flex;justify-content:space-between;font-family:"Jost",sans-serif;font-weight:700;font-size:140px;line-height:140px;color:#dcdcdc}
.avatar{position:absolute;left:67px;top:20px;width:93px;height:93px;border-radius:50%;border:3px solid #e4e4e4;background:radial-gradient(circle at 50% 40%,#c9a58a,#7c5e4b)}
.testimonial-text{position:absolute;left:12px;top:127px;width:204px;font-style:italic;font-size:10px;line-height:18px;color:#333}
.testimonial-name{display:block;font-style:normal;color:var(--pink)}

/* footer */
.site-footer{top:1970px;left:0;width:1200px;height:244px;background:var(--black)}
.footer-col{top:30px}
.footer-col h4{font-family:"Arimo",sans-serif;font-weight:400;color:var(--teal);font-size:11px;margin-bottom:6px}
.footer-col li{list-style:none;font-size:9px;line-height:18px;color:#ddd}
.social li{display:flex;align-items:center;gap:9px}
.social i{width:13px;height:13px;border-radius:50%;background:#ddd;display:block}
.footer-rule{left:241px;top:170px;width:718px;height:1px;background:#333}
.footer-note{left:0;width:1200px;text-align:center;font-size:8.5px;color:#777}
</style>
</head>
<body>

<header class="brand abs">
  <span class="brand-mark"></span>
  <span class="brand-name">CORVELLA</span>
</header>

<nav class="main-nav abs">
  <ul>
    <li class="is-active">Home</li>
    <li>Plans &amp; Pricing</li>
    <li>Features</li>
    <li>Phones</li>
    <li>Resource</li>
    <li>Blog</li>
  </ul>
</nav>

<section class="hero abs">
  <svg class="hero-band abs" viewBox="0 0 1200 594" aria-hidden="true">
    <polygon points="0,330 1200,242 1200,594 0,594" fill="#f07620"/>
    <polygon points="0,322 1200,236 1200,252 0,342" fill="#c85c12"/>
  </svg>
  <div class="video abs">
    <div class="video-frame" role="img" aria-label="Explainer video still: dim monochrome scene with string lights and a person">
      <svg class="video-play" width="64" height="64" viewBox="0 0 64 64" aria-hidden="true">
        <circle cx="32" cy="32" r="31" fill="rgba(0,0,0,.45)"/>
        <polygon points="25,18 48,32 25,46" fill="#bbb"/>
      </svg>
      <div class="video-bar">00:00 / 10:46</div>
    </div>
  </div>
</section>
<h1 class="hero-title abs">FIND US IN YOUR CITY</h1>
<p class="hero-sub abs">SERVING OVER 950 CANADIAN CITIES</p>
<a class="quote-btn abs">GET A QUOTE ONLINE!</a>

<section class="welcome abs">
  <span class="welcome-mark abs"></span>
  <h2 class="section-title abs">WELCOME TO CORVELLA</h2>
  <p class="welcome-copy abs">Cras accumsan orci mauris, ut aliquam ipsum faucibus sed. Fusce quam dui, accumsan a magna in, faucibus tristique lectus. Vestibulum sapien leo, placerat quis luctus eget, auctor et justo. Vestibulum ante ipsum primis in faucibus orci luctus et ultrices posuere cubilia Curae; Duis sagittis, risus ut viverra dignissim, lectus nunc iaculis arcu, et gravida est tortor ut erat. Morbi a feugiat dolor, in tristique elit.</p>
</section>

<section class="clients abs">
  <span class="clients-divider abs"></span>
  <h2 class="section-title abs">OUR CLIENTS</h2>
  <p class="clients-lead abs">Maecenas orci est, euismod facilisis feugiat sit amet, semper ut tortor.<br>Donec eleifend accumsan nisl, nec laoreet leo iaculis sit amet.</p>
  <div class="client-logo abs" style="left:244px">Halden's</div>
  <div class="client-logo abs" style="left:365px;font-size:11px">Visit Marrow Bay</div>
  <div class="client-logo abs" style="left:486px">Stonewick</div>
  <div class="client-logo abs" style="left:607px"><i></i>Blendora</div>
  <div class="client-logo abs" style="left:728px">Oatfield</div>
  <div class="client-logo abs" style="left:849px">Lumacare</div>
</section>

<section class="demo abs">
  <h2 class="section-title abs">SIGN UP FOR A PERSONALIZED DEMO.</h2>
  <p class="demo-copy abs">A member of Corvella's marketing team will contact you to discuss your specific situation and see if Corvella's Hosted PBX is a good fit for your organization. Alternatively, give us a call at <b>613-555-0142</b> to speak to someone immediately.</p>
  <div class="field abs" style="left:241px;top:149px">First Name</div>
  <div class="field abs" style="left:484px;top:149px">Last Name</div>
  <div class="field abs" style="left:726px;top:149px;width:233px">Company</div>
  <div class="field abs" style="left:241px;top:200px">Phone</div>
  <div class="field abs" style="left:484px;top:200px">Email</div>
  <a class="demo-btn abs">REQUEST A DEMO</a>
</section>

<section class="testimonials abs">
  <h2 class="section-title abs">“TESTIMONIALS”</h2>
  <article class="testimonial abs" style="left:241px">
    <div class="testimonial-quotes" aria-hidden="true"><span>“</span><span>”</span></div>
    <div class="avatar" role="img" aria-label="Portrait photo of a smiling man in a red cap"></div>
    <p class="testimonial-text">Cras accumsan orci mauris, ut aliquam ipsum faucibus sed. Fusce quam dui, accumsan a magna in, faucibus tristique lectus. Vestibulum sapien leo, placerat quis luctus eget, auctor et justo. Vestibulum ante ipsum primis in faucibus orci luctus et ultrices posuere cubilia Curae; Duis sagittis, risus ut viverra dignissim<span class="testimonial-name">Owen Harlan</span><span class="testimonial-name">Perth</span></p>
  </article>
  <article class="testimonial abs" style="left:486px">
    <div class="testimonial-quotes" aria-hidden="true"><span>“</span><span>”</span></div>
    <div class="avatar" role="img" aria-label="Portrait photo of a dark-haired man" style="background:radial-gradient(circle at 50% 40%,#d6b49a,#3a302a)"></div>
    <p class="testimonial-text">Sed quis nisl euismod, fermentum tellus a, lobortis quam. Vestibulum condimentum mi vitae diam tristique, egestas dignissim diam mattis. Curabitur vel diam in massa porttitor dictum id in lorem. Vivamus faucibus ac leo ac dignissim. Maecenas orci est, euismod facilisis feugiat sit amet, semper ut tortor. Donec eleifend<span class="testimonial-name">Dean Castell</span><span class="testimonial-name">New York</span></p>
  </article>
  <article class="testimonial abs" style="left:731px">
    <div class="testimonial-quotes" aria-hidden="true"><span>“</span><span>”</span></div>
    <div class="avatar" role="img" aria-label="Portrait photo of a woman with long brown hair" style="background:radial-gradient(circle at 50% 40%,#e2c0a6,#6b4a36)"></div>
    <p class="testimonial-text">Vivamus eu magna rhoncus, consectetur metus ac, varius lacus. Donec ultricies, tortor quis sagittis sagittis, mauris erat ullamcorper augue, eu placerat diam nunc a lorem. Nam vulputate mauris id arcu pharetra, sed posuere quam cursus. Nullam eget massa vel mi posuere venenatis sed quis tortor<span class="testimonial-name">Mara Quinlan</span><span class="testimonial-name">London</span></p>
  </article>
</section>

<footer class="site-footer abs">
  <div class="footer-col abs" style="left:241px">
    <h4>FEATURES &amp; BENEFITS</h4>
    <ul><li>Included Features</li><li>Optional Features</li><li>Conferencing</li><li>Can I keep my Phone Number?</li><li>Corvella VoIP Phones</li><li>Money Back Guarantee</li></ul>
  </div>
  <div class="footer-col abs" style="left:452px">
    <h4>RESOURCES</h4>
    <ul><li>What is Hosted PBX</li><li>Frequently Asked Questions</li><li>Testimonials</li><li>611 Online</li><li>Dashboard</li></ul>
  </div>
  <div class="footer-col abs" style="left:635px">
    <h4>CORVELLA</h4>
    <ul><li>Contact Us</li><li>Media Resources</li><li>Our History</li><li>Jobs</li><li>Corvella Vibe</li><li>Corvella Conversations, our Blog</li></ul>
  </div>
  <div class="footer-col social abs" style="left:821px">
    <h4>SOCIAL</h4>
    <ul><li><i></i>Friendwall</li><li><i></i>Chirper</li><li><i></i>Searchly</li><li><i></i>Vidstream</li><li><i></i>Worknet</li></ul>
  </div>
  <span class="footer-rule abs"></span>
  <p class="footer-note abs" style="top:188px">Call 1.877.55.CORVA or email sales@corvella.com.</p>
  <p class="footer-note abs" style="top:205px">Copyright © 2014 Corvella. All rights reserved. This site has a Privacy policy.</p>
</footer>

</body>
</html>
```